Specialist Technical Theatre service for schools

The task is to design a brochure (A5, 4 pages) for mailing to secondary/high school heads and drama departments to sell them our services as Technical Theatre and Drama professionals who can help them to offer elements of a curriculum that they do not currently offer as well as raise the technical standards of their school productions.
Please find a document attached which outlines the content for the brochure. Please read the document first so that you understand our aims. The text highlighted in yellow takes priority - the text highlighted in blue could be used if there is space.
Photos which may be used available on https://www.pictaro.com/photos/ben_tovey/ (please do not use watermarked nordel images).
Logo is attached (two variants) - one of which should appear somewhere on the design. Website address is www.bentovey.co.uk and email is info@bentovey.co.uk
Target Market(s)
Theatre and Drama teachers in Secondary/High schools
Headteachers of Secondary/High Schools
Industry/Entity Type
Education
Look and feel

```html
<!DOCTYPE html>
<html lang="en">
<head>
<meta charset="utf-8">
<title>Technical Theatre for Schools – Brochure Spread</title>
<link rel="stylesheet" href="https://fonts.googleapis.com/css2?family=Source+Sans+3:ital,wght@0,400;0,600;1,600;1,700&family=PT+Sans+Narrow:wght@700&display=swap">
<style>
  :root {
    --desk: #8e8d8e;
    --page: #1f1d1e;
    --ink: #f2f2f2;
    --accent-red: #d83a28;
    --folio: #111;
    --fold: #ffffff;
  }
  * { margin: 0; padding: 0; box-sizing: border-box; }
  html, body { width: 1200px; height: 1200px; overflow: hidden; background: var(--desk); }
  .canvas { position: relative; width: 1200px; height: 1200px; background: var(--desk); }

  .spread {
    position: absolute; left: 71px; top: 102px; width: 1064px; height: 752px;
    background: var(--page);
    font-family: "Source Sans 3", "Myriad Pro", sans-serif;
    color: var(--ink);
  }
  .stage-glow {
    position: absolute; left: 0; top: 0; width: 1064px; height: 230px;
    background:
      radial-gradient(circle at 345px 26px, rgba(230,200,60,.95) 0 26px, rgba(200,170,40,.35) 40px, transparent 60px),
      radial-gradient(circle at 461px 26px, rgba(60,150,200,.9) 0 26px, rgba(40,120,170,.35) 40px, transparent 60px),
      radial-gradient(circle at 877px 30px, rgba(100,110,220,.9) 0 26px, rgba(60,110,190,.35) 42px, transparent 62px),
      radial-gradient(circle at 989px 30px, rgba(230,150,150,.9) 0 22px, rgba(220,200,70,.55) 40px, transparent 64px),
      linear-gradient(#151313, rgba(31,29,30,0));
  }

  .body-copy {
    position: absolute; font-size: 12px; line-height: 15.2px;
    text-align: justify; hyphens: auto;
  }
  .body-copy p + p { margin-top: 14px; }

  .intro { left: 53px; top: 104px; width: 384px; }

  .question {
    position: absolute; left: 53px; width: 224px;
    font-family: "PT Sans Narrow", "Myriad Pro Condensed", sans-serif;
    font-weight: 700; font-size: 11.2px; line-height: 15.2px; text-align: justify;
  }
  .q1 { top: 314px; }
  .q2 { top: 381px; }
  .q3 { top: 452px; }

  .call-out {
    position: absolute; left: 91px; top: 559px; width: 134px;
    font-style: italic; font-weight: 600; font-size: 17px; line-height: 21.6px;
    color: var(--accent-red); text-align: justify; text-align-last: justify;
  }
  .call-out span { display: block; }
  .call-out .last { text-align-last: left; }

  .photo { position: absolute; }
  .photo-nativity { left: 340px; top: 316px; width: 135px; height: 98px;
    background: linear-gradient(135deg, #6a4a2c, #b88a4c 45%, #8a5a3a); }
  .photo-dancers { left: 300px; top: 459px; width: 293px; height: 220px;
    background: radial-gradient(ellipse at 40% 95%, #e8d8a0 0, transparent 35%),
                linear-gradient(160deg, #3e5f8e, #6b7fa8 40%, #4a4f70 70%, #2c2b3c); }
  .photo-concert { left: 513px; top: 326px; width: 96px; height: 68px;
    background: radial-gradient(ellipse at 50% 10%, #d0e4ff, #4a5ea0 45%, #15163a); }
  .photo-desk { left: 609px; top: 326px; width: 24px; height: 68px;
    background: linear-gradient(#3a4a5a, #0e1a1e 60%, #17402a); }
  .photo-stage { left: 641px; top: 326px; width: 58px; height: 68px;
    background: linear-gradient(#c05a3a, #5a2a20 60%, #1a1a16); }
  .photo-camp { left: 700px; top: 326px; width: 100px; height: 68px;
    background: linear-gradient(135deg, #5a5a44, #2e3026 60%, #1a1c16); }
  .photo-square { left: 802px; top: 326px; width: 103px; height: 68px;
    background: linear-gradient(#7da6d8 0 30%, #b8a890 30% 55%, #9a5a5a 55%); }
  .photo-cloaks { left: 905px; top: 228px; width: 159px; height: 166px;
    background: linear-gradient(100deg, #6a5e4e, #c8b49a 35%, #3a2e26 70%, #1a1612); }

  .credentials { left: 583px; top: 98px; width: 307px; }
  .credentials ul { list-style: none; }
  .credentials li { text-align: justify; }
  .credentials li::before { content: "•"; margin-right: 7px; margin-left: 2px; }

  .offer { left: 634px; top: 456px; width: 342px; }

  .fold { position: absolute; left: 598px; top: 0; width: 1px; height: 1200px; background: var(--fold); }

  .folio {
    position: absolute; top: 884px;
    font-family: "PT Sans Narrow", sans-serif; font-weight: 700; font-size: 32px; color: var(--folio);
  }
  .folio-left { left: 317px; }
  .folio-right { left: 881px; }
</style>
</head>
<body>
<div class="canvas">
  <section class="spread">
    <div class="stage-glow" role="img" aria-label="Out-of-focus coloured stage lights"></div>

    <div class="body-copy intro">
      <p>As live theatre and performance becomes an increasingly important part of the global economy, there is currently a huge demand for Technical and Production Management professionals. We are able to support you with training your students in the specialist skills and knowledge of managing creative processes from initial concept through rehearsal to realised performance.</p>
      <p>With 60% of marks being allocated to the practical elements of ‘creating original drama’ and ‘making theatre’ you would like to offer your students the opportunity to pursue the technical design elements of the course but don’t have the technical support? Northgate Exams A-level Drama and Theatre and Pemberton GCSE Drama (from September 2016)</p>
    </div>

    <p class="question q1">You would like someone with the specialist knowledge to ensure that your students meet the assessment criteria?</p>
    <p class="question q2">Your school and Drama Department owns a wide range of technical theatre equipment that isn’t used to its full potential?</p>
    <p class="question q3">You have a school wide musical, play or dance performance approaching and would like to get a student crew motivated, trained and involved in the technical aspects of the performance?</p>

    <p class="call-out"><span>If your answer to</span><span>any of the above</span><span>is ‘yes’ then we</span><span class="last">can help.</span></p>

    <div class="photo photo-nativity" role="img" aria-label="Photo of a costumed nativity scene on stage"></div>
    <div class="photo photo-dancers" role="img" aria-label="Photo of dancers in harlequin costumes under stage lights"></div>
    <div class="photo photo-concert" role="img" aria-label="Photo of a performance group under bright stage lighting"></div>
    <div class="photo photo-desk" role="img" aria-label="Photo of a lighting control desk"></div>
    <div class="photo photo-stage" role="img" aria-label="Photo of a stage lit in red"></div>
    <div class="photo photo-camp" role="img" aria-label="Photo of young actors in an outdoor scene"></div>
    <div class="photo photo-square" role="img" aria-label="Photo of a crowd at an outdoor event in a city square"></div>
    <div class="photo photo-cloaks" role="img" aria-label="Photo of three performers in dark cloaks"></div>

    <div class="body-copy credentials">
      <ul>
        <li>CRV checked staff (subscribed to the CRV update service so you can run an instant check on our arrival)</li>
        <li>Qualified in Technical Theatre (through a Stagecraft Board accredited establishment)</li>
        <li>ISWP certified (we adopt the latest safe working practice)</li>
        <li>First Aid Qualified (just in case!)</li>
        <li>Experience of working with Children and Young People in Education (includes previous experience of teaching production skills to GCSE and A-Level students and Youth theatre)</li>
        <li>Currently working in the Theatre and Events Industry (we bring current industry knowledge to you and your students)</li>
      </ul>
    </div>

    <div class="body-copy offer">
      <p>Whether its technical assistance with a one-off school production, practical examination performance support, weekly Technical Theatre Design curriculum delivery or workshops introducing Year 9 to the opportunities offered through Drama GCSE we can help you to find a solution.</p>
      <p>Budget tight? From £250 to £380 per day* depending on the requirement we are experts at working to academic budgets. We will always deliver the aims of the course using your school and department equipment; however, in order to ensure that your students are familiar with the latest technology we do include any specialist equipment (i.e LED lighting, Lumen editing suite, smoke machines etc.) within the cost.<br>*discount available if booking consecutive days, mileage charges apply.</p>
    </div>
  </section>

  <div class="fold"></div>
  <span class="folio folio-left">2</span>
  <span class="folio folio-right">3</span>
</div>
</body>
</html>
```